Packaging Design job - Health Supplement

We need a packaging design theme for a health supplement for Moroccan consumers. Our product is called 'Velmarine'. https://corvelsante.example/nos-produits/digestion/vel-marine/

It is a unique solution of three plants with recognized benefits. The activated carbon in the product allows, like plants, reduce effectively the problems related to digestion. The product is particularly effective for soothing bloating and optimizing intestinal transit as well as digestion.

We would like to see clean, modern and fresh designs.
This should give the impression of professional products of pharmaceutical quality.

You will find attached the current packaging design of the product. what we do not like:
- The design is not modern
- The design does not evoke the purpose of the product

You will also find attached the logo of our company.

Ps : You can change the color of the logo

Font styles to use
Serif
Sans Serif

Colors

Designer to choose colors to be used in the design.

Requirements
Must have
• - Bottle and box packaging required.
• - Product is bottle of 30 tablets
Should not have
• Sales and other "must buy" "guaranteed" etc

```html
<!DOCTYPE html>
<html lang="fr">
<head>
<meta charset="utf-8">
<title>Velmarine – Corvelsante</title>
<link rel="stylesheet" href="https://fonts.googleapis.com/css2?family=Tinos:wght@400&family=Arimo:wght@400;700&display=swap">
<style>
  :root {
    --red: #e8333a;
    --red-deep: #8a2a2e;
    --ink: #333132;
    --grey: #8e8e8e;
    --paper: #f1f1f1;
    --silver-light: #f4f4f4;
    --silver-mid: #d6d6d8;
    --silver-dark: #b9b9bc;
    --stage: #ffffff;
  }
  * { box-sizing: border-box; margin: 0; padding: 0; }
  html, body { width: 1200px; height: 967px; overflow: hidden; background: var(--stage); }
  .canvas { position: relative; width: 1200px; height: 967px; font-family: "Arimo", Arial, sans-serif; }

  /* ---------- Box ---------- */
  .box-front {
    position: absolute; left: 137px; top: 125px; width: 393px; height: 705px;
    background: var(--paper); overflow: hidden;
  }
  .box-side {
    position: absolute; left: 530px; top: 125px; width: 115px; height: 705px;
    background: linear-gradient(90deg, var(--red) 0%, #c52d33 55%, var(--red-deep) 100%);
    display: flex; align-items: center; justify-content: center;
  }
  .side-name {
    font-family: "Tinos", "Times New Roman", serif; font-size: 52px; color: #d9d9d9;
    transform: rotate(-90deg); white-space: nowrap; letter-spacing: 1px;
  }

  .brand { position: absolute; white-space: nowrap; }
  .brand-name { font-weight: 700; color: var(--red); line-height: 1; letter-spacing: 0.3px; }
  .brand-tagline { color: var(--ink); letter-spacing: 0.2px; margin-top: 3px; }
  .box-front .brand { left: 200px; top: 30px; }
  .box-front .brand-name { font-size: 25px; }
  .box-front .brand-tagline { font-size: 5.5px; }

  .product-name {
    position: absolute; font-family: "Tinos", "Times New Roman", serif; font-weight: 400;
    color: var(--red); line-height: 1; white-space: nowrap;
  }
  .ingredients { position: absolute; font-weight: 700; color: var(--grey); white-space: nowrap; }
  .benefits { position: absolute; list-style: none; color: #fff; white-space: nowrap; }
  .count { position: absolute; color: #fff; }
  .stomach-visual {
    position: absolute; border-radius: 30px 30px 60px 60px;
    background: linear-gradient(160deg, #ef5a60, #e23b42);
  }
  .band { position: absolute; }

  .box-front .product-name { left: 32px; top: 245px; font-size: 46px; }
  .box-front .ingredients { left: 33px; top: 296px; font-size: 17px; line-height: 25px; }
  .box-front .band { left: 0; top: 357px; width: 393px; height: 45px; }
  .box-front .red-panel { position: absolute; left: 0; top: 410px; width: 393px; height: 295px; background: var(--red); }
  .box-front .benefits { left: 33px; top: 437px; font-size: 16px; line-height: 21px; }
  .box-front .stomach-visual { left: 218px; top: 432px; width: 155px; height: 245px; }
  .box-front .count { left: 33px; top: 642px; font-size: 15px; }

  /* ---------- Jar ---------- */
  .jar-lid {
    position: absolute; left: 680px; top: 160px; width: 405px; height: 125px;
    border-radius: 40px 40px 6px 6px;
    background: linear-gradient(180deg, #fbfbfb 0%, #e6e6ea 60%, #cfcfd4 100%);
  }
  .jar-body {
    position: absolute; left: 676px; top: 285px; width: 414px; height: 510px;
    border-radius: 0 0 30px 30px;
    background: linear-gradient(90deg, var(--silver-dark) 0%, var(--silver-light) 30%, var(--silver-mid) 70%, var(--silver-dark) 100%);
    overflow: hidden;
  }
  .jar-body .brand { left: 202px; top: 32px; }
  .jar-body .brand-name { font-size: 19px; }
  .jar-body .brand-tagline { font-size: 4.5px; }
  .jar-body .product-name { left: 80px; top: 182px; font-size: 35px; }
  .jar-body .ingredients { left: 81px; top: 219px; font-size: 13.5px; line-height: 17px; }
  .jar-body .band { left: 59px; top: 255px; width: 290px; height: 36px; }
  .jar-body .red-panel { position: absolute; left: 59px; top: 293px; width: 286px; height: 195px; background: var(--red); }
  .jar-body .benefits { left: 82px; top: 317px; font-size: 12.5px; line-height: 16px; }
  .jar-body .stomach-visual { left: 219px; top: 315px; width: 105px; height: 170px; border-radius: 20px 20px 40px 40px; }
  .jar-body .count { left: 82px; top: 469px; font-size: 11.5px; }
</style>
</head>
<body>
<main class="canvas">
  <!-- Box -->
  <section class="box-front">
    <div class="brand">
      <div class="brand-name">CORVELSANTE</div>
      <div class="brand-tagline">HYGIÈNE PHARMACEUTIQUE ET DIÉTÉTIQUE</div>
    </div>
    <h1 class="product-name">VELMARINE</h1>
    <p class="ingredients">FENOUIL - ANIS VERT - CARVI NOIR<br>CHARBON VEGETAL ACTIVE</p>
    <svg class="band" viewBox="0 0 393 45" preserveAspectRatio="none" aria-hidden="true">
      <polygon points="0,0 305,0 333,45 0,45" fill="var(--ink)"/>
      <polygon points="315,0 393,0 393,18 326,18" fill="var(--red)"/>
    </svg>
    <div class="red-panel"></div>
    <ul class="benefits">
      <li>Facilite Le Transit</li>
      <li>Ameliore La Digestion</li>
      <li>Effect Ventre Plant</li>
    </ul>
    <div class="stomach-visual" role="img" aria-label="White line drawing of a stomach and digestive tract"></div>
    <p class="count">30 Gelules</p>
  </section>
  <aside class="box-side">
    <span class="side-name">VELMARINE</span>
  </aside>

  <!-- Jar -->
  <div class="jar-lid"></div>
  <section class="jar-body">
    <div class="brand">
      <div class="brand-name">CORVELSANTE</div>
      <div class="brand-tagline">HYGIÈNE PHARMACEUTIQUE ET DIÉTÉTIQUE</div>
    </div>
    <h2 class="product-name">VELMARINE</h2>
    <p class="ingredients">FENOUIL - ANIS VERT - CARVI NOIR<br>CHARBON VEGETAL ACTIVE</p>
    <svg class="band" viewBox="0 0 290 36" preserveAspectRatio="none" aria-hidden="true">
      <polygon points="0,0 222,0 244,36 0,36" fill="var(--ink)"/>
      <polygon points="232,0 290,0 290,14 240,14" fill="var(--red)"/>
    </svg>
    <div class="red-panel"></div>
    <ul class="benefits">
      <li>Facilite Le Transit</li>
      <li>Ameliore La Digestion</li>
      <li>Effect Ventre Plant</li>
    </ul>
    <div class="stomach-visual" role="img" aria-label="White line drawing of a stomach and digestive tract"></div>
    <p class="count">30 Gelules</p>
  </section>
</main>
</body>
</html>
```